I am looking for a designer for my Gratitude Journal cover design. This is a daily gratitude journal designed for women. The interior features colored pages with a daily gratitude section, weekly habit tracker, and monthly reflection. The journal has enough space for a 12-week journaling.
Book size: 6x 9 inches
Paperback Print Book
Page count: 117
Platform: Pemberly Press
Book title: Bloom Anyway, Dear
Design Style:
-Boho style color and graphics, color choice is free but must follow color psychology, no pure black. The color and styling should correlate to the interior pages (In the attachment).
-There could be a female silhouette on the front cover, but not as big as the whole cover. (doesn’t have to if not looking good)
-No text or interior page preview on the back cover. Only pen name logo on the bottom middle of the back cover and make it small and subtle. (Pen name logo attached)
-Book title on front cover and spine, author name only on spine (Author name: Tobin Vasque).
-No other text on the front cover.
All design elements including fonts must be commercially licensed, and you must provide source files and commercial licenses of them together as part of the delivery.
Target Market(s)
pemberlypress.example

```html
<!DOCTYPE html>
<html lang="en">
<head>
<meta charset="utf-8">
<title>Bloom Anyway, Dear — Cover Wrap</title>
<link href="https://fonts.googleapis.com/css2?family=Smokum&family=Oswald:wght@400&display=swap" rel="stylesheet">
<style>
  :root {
    --paper: #fdf9ea;
    --spine: #f2adab;
    --coral: #e2674f;
    --leaf: #7fae44;
    --sun: #f6c54a;
    --sky: #3fb0e0;
    --ink-navy: #2b3357;
    --spine-ink: #7a4a1e;
    --frame: #f0c58a;
    --display: "Smokum", "Oswald", "Arial Narrow", sans-serif;
  }
  * { box-sizing: border-box; margin: 0; padding: 0; }
  html, body { width: 1200px; height: 887px; overflow: hidden; background: var(--paper); }
  .cover-wrap { position: relative; width: 1200px; height: 887px; background: var(--paper); }

  .art { position: absolute; border-radius: 6px; }
  .back-dreamcatcher {
    left: 42px; top: 22px; width: 505px; height: 658px;
    background: linear-gradient(180deg, rgba(246,197,74,.45) 0%, rgba(240,142,60,.35) 45%, rgba(127,174,68,.28) 70%, rgba(63,176,224,.3) 100%);
    border-radius: 50% 50% 30% 30% / 40% 40% 20% 20%;
  }
  .barcode-frame {
    position: absolute; left: 371px; top: 735px; width: 192px; height: 115px;
    border: 1px solid var(--frame);
  }
  .pen-mark {
    position: absolute; left: 293px; top: 808px; transform: translateX(-50%);
    display: flex; align-items: center; gap: 6px; white-space: nowrap;
    font-family: var(--display); font-size: 15px; line-height: 1; color: var(--ink-navy);
    letter-spacing: .5px;
  }
  .pen-mark .dot { width: 12px; height: 12px; border-radius: 50%; background: var(--ink-navy); flex: none; }

  .spine {
    position: absolute; left: 587px; top: 0; width: 25px; height: 887px; background: var(--spine);
  }
  .spine-text {
    position: absolute; left: 50%; top: 760px;
    transform: translate(-50%, -50%) rotate(-90deg);
    white-space: nowrap; font-family: var(--display); font-size: 13px; line-height: 1; color: var(--spine-ink);
  }
  .spine-text .gap { display: inline-block; width: 12px; }

  .hanging-feathers-left {
    left: 630px; top: 0; width: 137px; height: 518px;
    background: linear-gradient(90deg, rgba(127,174,68,.28), rgba(63,176,224,.3));
    border-radius: 0 0 40px 40px;
  }
  .sun-flower {
    left: 828px; top: 48px; width: 141px; height: 134px;
    background: radial-gradient(circle, #f3a23a 0%, #f7d67a 55%, rgba(246,197,74,.7) 75%, transparent 76%);
    border-radius: 50%;
  }
  .hanging-feathers-right {
    left: 1048px; top: 0; width: 122px; height: 560px;
    background: linear-gradient(90deg, rgba(246,197,74,.35), rgba(226,103,79,.35));
    border-radius: 0 0 40px 40px;
  }
  .woman-silhouette {
    left: 716px; top: 518px; width: 333px; height: 369px;
    background: linear-gradient(160deg, #3a4570 0%, var(--ink-navy) 55%, #d9683f 100%);
    border-radius: 45% 45% 10px 10px;
  }

  .title {
    position: absolute; left: 776px; top: 236px; width: 268px;
    font-family: var(--display); line-height: 1; font-weight: 400; font-stretch: condensed;
  }
  .title-line-one { display: block; white-space: nowrap; color: var(--coral); font-size: 56px; }
  .title-line-two { display: block; white-space: nowrap; color: var(--leaf); font-size: 104px; margin-top: 14px; }
</style>
</head>
<body>
<main class="cover-wrap">
  <section class="back-cover">
    <div class="art back-dreamcatcher" role="img" aria-label="Boho dreamcatcher hanging from an arrow, with beads and feathers in yellow, orange, green and blue"></div>
    <div class="barcode-frame"></div>
    <div class="pen-mark"><span class="dot"></span><span>TOBIN VASQUE</span></div>
  </section>

  <section class="spine">
    <p class="spine-text">Tobin Vasque<span class="gap"></span>Bloom Anyway, Dear</p>
  </section>

  <section class="front-cover">
    <div class="art hanging-feathers-left" role="img" aria-label="Hanging green and blue feathers on beaded strings"></div>
    <div class="art sun-flower" role="img" aria-label="Yellow boho sun flower"></div>
    <div class="art hanging-feathers-right" role="img" aria-label="Hanging yellow and coral feathers on beaded strings"></div>
    <h1 class="title">
      <span class="title-line-one">Bloom Anyway,</span>
      <span class="title-line-two">Dear</span>
    </h1>
    <div class="art woman-silhouette" role="img" aria-label="Profile silhouette of a woman with a patterned headscarf, hoop earring and glasses"></div>
  </section>
</main>
</body>
</html>
```